Emerging automotive detailing business

I am starting a small automotive detailing business in hopes of becoming a well-known detailer to work on high end cars. I would like a card to reflect the high quality and time I put into my work. The name of the company is Brightmere Detailing. I feel like it represents racecars getting off the line at the drag strip as well as an innuendo of "Off the Charts". I do minor paint correction such as clay barring, multi-step buffing and polishing, waxing, hand washes, etc. I am always striving to learn more and improve my work. My goal is to have total customer satisfaction. This is a female run business but I do not want it to be very girly. Elegant is okay! I have pictures of my personal kestrel attached, they do not need to be incorporated but if you can think of a cool way to use 1 or all of them, go for it!

Target Market(s)

Anyone that owns a vehicle. Preferably high end vehicles such as Valdren, Castavelli and Moretto but I will also happily work on any car, truck or suv no matter what brand.

Industry/Entity Type

Automotive

Contact Information for Business Card

Brightmere Detailing
Nora Pellworth
4715 Quillbrook Rd
Red Lion PA 17392
Cell phone- call/text- 717-555-0148
email- brightmeredetails@example.com
Instagram: @brightmeredetailing
Facebook: facebook.example/brightmeredetailing

Requirements
Must have
• Business name, my name, address, phone number. Listing that I do minor paint correction such as clay barring, multi-step buffing and polishing, waxing, hand washes, interior cleaning, and more. (This last part was in nice to haves but I have realized that I do really want it, so I moved it to must haves.) I want something that is different and eye-catching to my customers. Some people have done this very well with cards already submitted to me, but a lot have not. I didn't mess with the "look and feel bars" much because because I am pretty open to the overall design as long as it is not your basic run of the mill design.
Nice to have
• Something car related. Maybe an appointment time/date line. I do not have a logo, but if you would like to design one and incorporate it, that would be amazing!
Should not have
• Purple and Pink colors. Boring, basic, normal card.

```html
<!DOCTYPE html>
<html lang="en">
<head>
<meta charset="utf-8">
<title>Brightmere Detailing – Business Card</title>
<link rel="stylesheet" href="https://fonts.googleapis.com/css2?family=Jost:wght@400;500;700&display=swap">
<style>
  :root {
    --page-bg: #d9d9d9;
    --card-black: #060606;
    --panel-light: rgba(236, 236, 236, 0.86);
    --ink: #111111;
    --rule: #1a1a1a;
    --white: #ffffff;
    --soft-white: #cfcfcf;
    --photo-green: #2f5a22;
    --photo-cream: #d9d4bd;
    --photo-blue: #1f3a4f;
  }
  html, body {
    margin: 0;
    padding: 0;
    width: 1200px;
    height: 1023px;
    overflow: hidden;
    background: var(--page-bg);
    font-family: "Jost", "Futura", sans-serif;
  }
  .canvas {
    position: relative;
    width: 1200px;
    height: 1023px;
  }
  .card {
    position: absolute;
    left: 300px;
    width: 600px;
    height: 343px;
    overflow: hidden;
    box-shadow: 0 6px 18px rgba(0,0,0,0.25);
  }
  .card--front { top: 120px; background: var(--card-black); }
  .card--back { top: 560px; background: var(--card-black); }

  .car-photo {
    position: absolute;
    inset: 0;
    background:
      linear-gradient(180deg, transparent 0%, transparent 72%, var(--photo-blue) 84%, #0d1a24 100%),
      linear-gradient(90deg, var(--photo-green) 0%, #4b6b3a 14%, var(--photo-cream) 30%, #bfb9a2 62%, #44505a 85%, #1b2a36 100%);
  }
  .card__corner {
    position: absolute;
    top: 0; left: 0;
    width: 60px;
    height: 44px;
    background: var(--card-black);
  }
  .appointment-panel {
    position: absolute;
    top: 0;
    left: 60px;
    right: 0;
    height: 290px;
    background: var(--panel-light);
  }
  .appointment {
    position: absolute;
    top: 26px;
    right: 30px;
    width: 240px;
    color: var(--ink);
  }
  .appointment__title {
    margin: 0;
    font-size: 25px;
    font-weight: 700;
    letter-spacing: 0.5px;
    border-bottom: 1.5px solid var(--rule);
    padding: 0 0 4px 18px;
  }
  .appointment__field {
    font-size: 17px;
    font-weight: 400;
    border-bottom: 1.5px solid var(--rule);
    padding: 10px 0 3px 0;
  }
  .services {
    position: absolute;
    left: 82px;
    top: 180px;
    width: 300px;
    margin: 0;
    padding: 0;
    list-style: none;
    color: var(--ink);
    font-size: 17px;
  }
  .services__row {
    display: flex;
    border-bottom: 1.5px solid var(--rule);
    padding: 8px 0 3px 0;
  }
  .services__item { white-space: nowrap; }
  .services__item::before { content: "• "; }
  .services__item--primary { width: 180px; }

  .brand {
    position: absolute;
    left: 0; right: 0;
    top: 56px;
    text-align: center;
    color: var(--white);
  }
  .brand__bar {
    width: 120px;
    height: 10px;
    margin: 0 auto 14px;
    background: var(--white);
  }
  .brand__name {
    display: inline-block;
    margin: 0;
    font-size: 34px;
    font-weight: 700;
    letter-spacing: 1px;
    padding: 0 18px 6px;
    border-bottom: 1.5px solid var(--white);
  }
  .contact {
    margin: 22px 0 0;
    font-style: normal;
    font-size: 15px;
    line-height: 1.5;
    color: var(--soft-white);
  }
  .contact__owner {
    display: block;
    font-size: 18px;
    font-weight: 500;
    color: var(--white);
    margin-bottom: 4px;
  }
</style>
</head>
<body>
<main class="canvas">
  <section class="card card--front" aria-label="Appointment side">
    <div class="car-photo" role="img" aria-label="Photo of a cream sports car parked beside green trees"></div>
    <div class="card__corner"></div>
    <div class="appointment-panel"></div>
    <div class="appointment">
      <h2 class="appointment__title">Appointment</h2>
      <div class="appointment__field">Date</div>
      <div class="appointment__field">Time</div>
    </div>
    <ul class="services">
      <li class="services__row"><span class="services__item services__item--primary">Multi-step buffing</span><span class="services__item">Polishing</span></li>
      <li class="services__row"><span class="services__item services__item--primary">Interior cleaning</span><span class="services__item">Waxing</span></li>
      <li class="services__row"><span class="services__item services__item--primary">Hand washes</span><span class="services__item">Clay barring</span></li>
    </ul>
  </section>

  <section class="card card--back" aria-label="Brand side">
    <div class="brand">
      <div class="brand__bar"></div>
      <h1 class="brand__name">Brightmere Detailing</h1>
      <address class="contact">
        <span class="contact__owner">Nora Pellworth</span>
        4715 Quillbrook Rd, Red Lion PA 17392<br>
        Call/Text 717-555-0148 · brightmeredetails@example.com
      </address>
    </div>
  </section>
</main>
</body>
</html>
```